Lumen Path - Fiber Internet to the home postcard

Design a postcard for my company, Lumen Path, using the logo below. On the front of the card:
- No Buffering • No BS
- Second line should be the logo
- $60 / month • 10-Gigs
- lumenpath.net

Color palate should follow the colors in the logo.

Address should say
- Special pricing during construction
- Our best price
- Our fastest speed
- $60 / month • 10-Gigs
- lumenpath.net

Target Market(s)

25 - 55 year olds. Middle income/class. People with kids and pick up trucks

Industry/Entity Type

Fiber Internet Service Provider

Font styles to use
Sans Serif

Colors

Designer to choose colors to be used in the design.

Requirements
Nice to have
• I am open to more creative changes

```html
<!DOCTYPE html>
<html lang="en">
<head>
<meta charset="utf-8">
<title>Lumen Path – Fiber Postcard</title>
<link href="https://fonts.googleapis.com/css2?family=Poppins:ital,wght@0,400;0,500;0,800;1,500;1,800&display=swap" rel="stylesheet">
<style>
  :root {
    --navy: #01295a;
    --green: #7ac043;
    --white: #ffffff;
  }
  * { margin: 0; padding: 0; box-sizing: border-box; }
  html, body { width: 884px; height: 1200px; overflow: hidden; background: var(--white); }
  body { font-family: "Poppins", sans-serif; }
  .card { position: relative; width: 884px; height: 1200px; }

  .front-top {
    position: absolute; left: 28px; top: 28px; width: 828px; height: 172px;
    background: var(--navy); color: var(--white);
    display: flex; align-items: center; justify-content: center;
    font-weight: 400; font-size: 70px; letter-spacing: 0.5px;
  }
  .divider {
    display: inline-block; width: 10px; height: 72px; background: currentColor;
    margin: 0 38px; vertical-align: middle; position: relative; top: -4px;
  }

  .brand {
    position: absolute; left: 28px; top: 218px; width: 828px; height: 136px;
    display: flex; align-items: center; justify-content: center;
  }
  .brand-name { font-weight: 500; font-size: 62px; color: var(--navy); letter-spacing: 0.5px; }

  .offer-band {
    position: absolute; left: 28px; top: 371px; width: 828px; height: 122px;
    background: var(--green); color: var(--white);
    display: flex; align-items: center; justify-content: center;
    font-weight: 800; font-style: italic; font-size: 64px; letter-spacing: -1px;
  }
  .offer-band .divider { width: 11px; height: 86px; margin: 0 40px; top: 8px; }

  .url-band {
    position: absolute; left: 28px; top: 493px; width: 828px; height: 86px;
    background: var(--navy); color: var(--white);
    display: flex; align-items: center; justify-content: center;
    font-weight: 500; font-style: italic; font-size: 34px;
  }

  .back {
    position: absolute; left: 28px; top: 618px; width: 828px; height: 551px;
    background: var(--green); overflow: hidden;
  }
  .back-shape { position: absolute; left: 0; top: 0; }
  .back-brand {
    position: absolute; left: 0; top: 248px; width: 300px; text-align: center;
    font-weight: 500; font-size: 40px; color: var(--white);
  }
  .back-copy {
    position: absolute; left: 340px; top: 96px; width: 470px;
    text-align: center; color: var(--white);
    font-style: italic; font-weight: 500; font-size: 37px; line-height: 62px;
  }
  .back-url {
    position: absolute; right: 34px; bottom: 14px; color: var(--white);
    font-style: italic; font-weight: 500; font-size: 31px;
  }
</style>
</head>
<body>
<div class="card">
  <header class="front-top">No Buffering<span class="divider"></span>No BS</header>

  <div class="brand">
    <span class="brand-name">Lumen Path</span>
  </div>

  <div class="offer-band">$60 / Month<span class="divider"></span>10-Gigs</div>
  <div class="url-band">lumenpath.net</div>

  <section class="back">
    <svg class="back-shape" width="828" height="551" viewBox="28 618 828 551" aria-hidden="true">
      <polygon fill="var(--navy)" points="457,618 856,618 856,1169 455,1169 439,1122 279,1122 360,894 279,664 441,664"/>
    </svg>
    <div class="back-brand">Lumen Path</div>
    <div class="back-copy">
      <p>Special Pricing During</p>
      <p>Construction</p>
      <p>Our best price</p>
      <p>Our fastest speed</p>
      <p>$60 / month</p>
      <p>10-Gigs</p>
    </div>
    <div class="back-url">lumenpath.net</div>
  </section>
</div>
</body>
</html>
```